Business Card Design Project

Hi,
This is a simple contest. The logo for the back of the card is deigned. See attached files. The front of the card must have :

Directors Name: Dorian
Mob:
e-mail:
Postal Address:
Web Page Adress:

It may also add words: "Leaders in Construction Project Management Services"

Target Market(s)

Business & Home owners alike

Industry/Entity Type

Business

Requirements
Must have
• See details above and logo attached
Should not have
• Images other than logo

```html
<!DOCTYPE html>
<html lang="en">
<head>
<meta charset="utf-8">
<title>Dorian — Business Card</title>
<link rel="stylesheet" href="https://fonts.googleapis.com/css2?family=Open+Sans:wght@300;400;800&display=swap">
<style>
  :root {
    --brand-blue: #1a9ad6;
    --card-white: #ffffff;
  }
  html, body {
    margin: 0;
    padding: 0;
    width: 1200px;
    height: 900px;
    overflow: hidden;
    background: var(--card-white);
  }
  .card {
    display: block;
    width: 1200px;
    height: 900px;
  }
  .director-name {
    font-family: "Open Sans", sans-serif;
    font-weight: 800;
    font-size: 98px;
    letter-spacing: -2px;
    fill: var(--brand-blue);
  }
  .director-title {
    font-family: "Open Sans", sans-serif;
    font-weight: 300;
    font-size: 33px;
    letter-spacing: 8px;
    fill: var(--brand-blue);
  }
  .divider {
    stroke: var(--brand-blue);
    stroke-width: 2;
  }
  .contact-label {
    font-family: "Open Sans", sans-serif;
    font-weight: 300;
    font-size: 50px;
    letter-spacing: -1px;
    fill: var(--brand-blue);
  }
  .brand-mark {
    fill: var(--brand-blue);
  }
  .brand-name {
    font-family: "Open Sans", sans-serif;
    font-weight: 400;
    font-size: 19px;
    fill: var(--brand-blue);
  }
  .tagline {
    font-family: "Open Sans", sans-serif;
    font-weight: 300;
    font-size: 22px;
    letter-spacing: -0.3px;
    fill: var(--brand-blue);
  }
</style>
</head>
<body>
<svg class="card" viewBox="0 0 1200 900" xmlns="http://www.w3.org/2000/svg">
  <g class="identity">
    <text class="director-name" x="245" y="468">DORIAN</text>
    <text class="director-title" x="247" y="500">DIRECTOR</text>
  </g>

  <line class="divider" x1="698" y1="262" x2="698" y2="612"/>

  <g class="contact-details">
    <text class="contact-label" x="785" y="332">MOBILE</text>
    <text class="contact-label" x="785" y="409">E-MAIL</text>
    <text class="contact-label" x="785" y="486">POSTAL</text>
    <text class="contact-label" x="785" y="562">WEB</text>
  </g>

  <g class="company-footer">
    <rect class="brand-mark" x="260" y="822" width="18" height="18"/>
    <text class="brand-name" x="284" y="838">Vantra</text>
    <text class="tagline" x="360" y="838">“LEADERS IN CONSTRUCTION PROJECT MANAGEMENT SERVICES”</text>
  </g>
</svg>
</body>
</html>
```